Letterhead for Business Law Firm

We need a letter head for our firm based on the design we have settled on and it is attached. Our clients are small and large businesses around the world, and our letterhead is used typically for formal legal purposes such as demand letters (accusing the recipient of doing bad things) or responding to demand letters. It may also be sent to regulators and other government agencies. So this needs to be tasteful, but a little edgy as well - we try to convey that we are a firm that is different - businesses and investors come to us for creative, quick advice, typically in high stress circumstances, and for our ability to work through high conflict situations, and rapid paced engagements.

Target Market(s)

Lawyers, business executives, investors, government regulators who may receive letters from this firm on behalf of its clients.

Industry/Entity Type

Business

Requirements
Must have
• The design and the firm's contact information:
• Quillfen Law Firm, P.C.
• 8716 SW 19th Ave
• Portland, OR 97058
• phone: 971 555 0143
• fax: 971 555 0178
• in what placement and how depicted (e.g. a phone icon instead of the word "phone") I leave to your creative ideas.
Nice to have
• design and information can be placed at the top, bottom and/or sides of the letter, and the design should be for a standard letter size paper - and can have a separate design for the second page.

```html
<!DOCTYPE html>
<html lang="en">
<head>
<meta charset="utf-8">
<title>Quillfen Law Firm, P.C. Letterhead</title>
<link rel="stylesheet" href="https://fonts.googleapis.com/css2?family=Old+Standard+TT:wght@400;700&display=swap">
<style>
  :root {
    --backdrop: #b9bcc0;
    --paper: #ffffff;
    --ink: #141010;
    --teal: #2a8593;
    --rule: #5fb6c1;
  }
  * { box-sizing: border-box; margin: 0; padding: 0; }
  html, body {
    width: 1200px;
    height: 1000px;
    overflow: hidden;
    background: var(--backdrop);
  }
  .sheet {
    position: absolute;
    left: 258px;
    top: 44px;
    width: 647px;
    height: 916px;
    background: var(--paper);
  }
  .letterhead {
    position: absolute;
    left: 169px;
    top: 31px;
    width: 310px;
    font-family: "Old Standard TT", "Times New Roman", serif;
    color: var(--ink);
  }
  .firm-name {
    display: block;
    height: 73px;
    line-height: 73px;
    text-align: center;
    font-size: 38px;
    font-weight: 400;
    letter-spacing: 0.28em;
    padding-left: 0.28em;
    color: var(--ink);
  }
  .contact {
    margin-top: 8px;
    font-size: 13px;
    line-height: 16px;
    font-style: normal;
    color: var(--ink);
  }
  .contact-row {
    display: flex;
    justify-content: space-between;
    white-space: nowrap;
  }
  .label {
    color: var(--teal);
    margin-right: 5px;
  }
  .footer-rule {
    position: absolute;
    left: 53px;
    top: 887px;
    width: 540px;
    height: 0;
    border-top: 1.5px solid var(--rule);
  }
</style>
</head>
<body>
  <main class="sheet">
    <header class="letterhead">
      <h1 class="firm-name">QUILLFEN</h1>
      <address class="contact">
        <div class="contact-row">
          <span><span class="label">A</span>8716 SW 19th Ave, Portland, OR 97058 USA</span>
        </div>
        <div class="contact-row">
          <span><span class="label">T</span>971 555 0143</span>
          <span><span class="label">M</span>971 555 0162</span>
          <span><span class="label">F</span>971 555 0178</span>
        </div>
        <div class="contact-row">
          <span><span class="label">E</span>ellis@quillfen.com</span>
          <span><span class="label">W</span>www.quillfen.com</span>
        </div>
      </address>
    </header>
    <div class="footer-rule"></div>
  </main>
</body>
</html>
```